Quilvo Garage Doors Business Card

I need a Business Card for my garage door business:
Quilvo Garage Doors.
please add:
logo
phone number: 855-3-QUILVO
(853-392)

email: service@quilvogaragedoors.com
website: www.quilvogaragedoors.com

The attached image is recommendation ONLY.

```html
<!DOCTYPE html>
<html lang="en">
<head>
<meta charset="utf-8">
<title>Quilvo Garage Doors – Business Card</title>
<link rel="stylesheet" href="https://fonts.googleapis.com/css2?family=Lato:wght@400;700;900&display=swap">
<style>
  :root {
    --teal: #5ec4cc;
    --teal-deep: #4fb3b5;
    --teal-pale: #c5e6ea;
    --card-white: #f7f7f6;
    --ink: #1f2326;
    --band-gray: #6b6b6b;
    --backdrop: #e2e1df;
    --white: #ffffff;
  }
  * { margin: 0; padding: 0; box-sizing: border-box; }
  html, body {
    width: 1200px; height: 720px; overflow: hidden;
    background: var(--backdrop);
    font-family: "Lato", Arial, sans-serif;
  }
  .card-sheet {
    position: relative; width: 1200px; height: 720px;
    display: flex; align-items: center; justify-content: center; gap: 40px;
  }
  .card {
    position: relative; width: 540px; height: 309px; overflow: hidden;
    box-shadow: 0 2px 6px rgba(0,0,0,0.12);
  }

  /* Front */
  .card-front { background: var(--card-white); }
  .front-art { position: absolute; inset: 0; }
  .brand {
    position: absolute; left: 44px; top: 78px;
    display: flex; align-items: center; gap: 16px;
  }
  .brand-square { width: 52px; height: 52px; background: var(--teal); }
  .brand-name {
    font-weight: 900; font-size: 25px; line-height: 1.05; color: var(--ink);
  }
  .contact {
    position: absolute; left: 46px; top: 150px;
    color: var(--teal); font-size: 15px; line-height: 1.15;
  }
  .contact-row { display: flex; align-items: flex-start; gap: 10px; margin-bottom: 16px; }
  .contact-row svg { flex: none; margin-top: 2px; }
  .website {
    position: absolute; left: 0; right: 0; bottom: 14px;
    text-align: center; padding-left: 70px;
    color: var(--teal); font-weight: 900; font-size: 15px;
  }

  /* Back */
  .card-back { background: var(--teal-deep); }
  .team-photo {
    position: absolute; inset: 0;
    background: linear-gradient(180deg, #58b9b8 0%, #62c2c0 55%, #5ab6b4 100%);
  }
  .back-brand {
    position: absolute; left: 0; right: 0; top: 110px;
    display: flex; align-items: center; justify-content: center; gap: 18px;
  }
  .back-brand .brand-square { background: var(--white); width: 62px; height: 62px; }
  .back-brand .brand-name { color: var(--white); font-size: 30px; }
</style>
</head>
<body>
<main class="card-sheet">

  <section class="card card-front" aria-label="Business card front">
    <svg class="front-art" width="540" height="309" viewBox="0 0 540 309" aria-hidden="true">
      <rect class="accent-bar" x="38" y="0" width="144" height="14" fill="var(--teal)"/>
      <circle class="corner-disc" cx="470" cy="80" r="92" fill="var(--teal-pale)"/>
      <path class="footer-band" d="M0 262 C150 252 340 236 540 222 L540 309 L0 309 Z" fill="var(--band-gray)"/>
      <path class="footer-swoosh" d="M0 272 C170 262 360 246 540 236" stroke="var(--card-white)" stroke-width="3" fill="none"/>
      <path class="footer-swoosh" d="M120 262 C260 252 400 240 540 230" stroke="var(--card-white)" stroke-width="1.5" fill="none"/>
    </svg>

    <div class="brand">
      <span class="brand-square"></span>
      <span class="brand-name">Quilvo<br>Garage Doors</span>
    </div>

    <div class="contact">
      <div class="contact-row">
        <svg width="14" height="14" viewBox="0 0 24 24" aria-hidden="true"><path fill="var(--teal)" d="M6.6 10.8c1.4 2.8 3.8 5.1 6.6 6.6l2.2-2.2c.3-.3.7-.4 1-.2 1.1.4 2.3.6 3.6.6.6 0 1 .4 1 1V20c0 .6-.4 1-1 1C10.6 21 3 13.4 3 4c0-.6.4-1 1-1h3.5c.6 0 1 .4 1 1 0 1.3.2 2.5.6 3.6.1.3 0 .7-.2 1z"/></svg>
        <span>855-3-QUILVO<br>(853-392)</span>
      </div>
      <div class="contact-row">
        <svg width="16" height="12" viewBox="0 0 16 12" aria-hidden="true"><rect x="0.5" y="0.5" width="15" height="11" fill="var(--teal)"/><path d="M1 1l7 6 7-6" stroke="var(--card-white)" stroke-width="1.2" fill="none"/></svg>
        <span>service@quilvogaragedoors.com</span>
      </div>
    </div>

    <p class="website">www.quilvogaragedoors.com</p>
  </section>

  <section class="card card-back" aria-label="Business card back">
    <div class="team-photo" role="img" aria-label="Teal-tinted photo of the service team standing beside a company truck in front of trees"></div>
    <div class="back-brand">
      <span class="brand-square"></span>
      <span class="brand-name">Quilvo<br>Garage Doors</span>
    </div>
  </section>

</main>
</body>
</html>
```